Flyer für Photovoltaik Anlagen
Zielgruppe
Wir bieten die Planung+Errichtung von Photovoltaik Anlagen und die dazugehörigen Komponenten wie Ladestationen und Speicher an
Aufgabenstellung
Ich habe eine erste Vorlage erstellt, die aber sehr überladen ist, ich will, dass auf Seite 1 schön und leicht verständlich dargestellt ist, was wir anbieten. Der Flyer soll beidseitig bedruckt sein

```html
<!DOCTYPE html>
<html lang="de">
<head>
<meta charset="utf-8">
<title>SOLVARA – Flyer Photovoltaik</title>
<link rel="stylesheet" href="https://fonts.googleapis.com/css2?family=Jost:wght@700&family=Open+Sans:ital,wght@0,400;0,600;0,700;1,700&display=swap">
<style>
  :root{
    --navy:#14151f;
    --gold:#eab54a;
    --gold-deep:#e39a45;
    --ink:#141414;
    --paper:#ffffff;
    --bg:#ffffff;
  }
  *{margin:0;padding:0;box-sizing:border-box}
  html,body{width:1200px;height:960px;overflow:hidden;background:var(--bg)}
  body{position:relative;font-family:"Open Sans",sans-serif;color:var(--ink)}
  .page{position:absolute;top:104px;width:548px;height:776px;background:var(--paper);overflow:hidden}
  .page--front{left:37px}
  .page--back{left:620px}
  .shapes{position:absolute;inset:0;width:548px;height:776px}
  .abs{position:absolute}

  /* front */
  .headline{left:41px;top:30px;font-family:"Jost",sans-serif;font-weight:700;font-size:35px;line-height:39px;color:var(--ink);letter-spacing:-.2px}
  .headline .accent{color:var(--gold)}
  .brand{left:370px;top:104px;width:180px;text-align:center;color:var(--gold);font-weight:700;font-size:20px;letter-spacing:4px}
  .brand-dot{left:442px;top:62px;width:34px;height:34px;border-radius:50%;background:var(--gold)}
  .polaroid{position:absolute;background:#fff;padding:6px;box-shadow:0 2px 6px rgba(0,0,0,.35)}
  .polaroid .fill{width:100%;height:100%}
  .intro{left:270px;top:452px;width:250px;color:#fff;font-size:10.2px;line-height:13.9px}
  .intro p{margin-bottom:11px}
  .intro .company{color:var(--gold);font-weight:700}
  .services-label{left:53px;top:532px;color:var(--gold);font-weight:700;font-size:10.5px}
  .services{left:53px;top:552px;list-style:none;color:#fff;font-size:16.5px}
  .services li{height:26.4px;display:flex;align-items:center}
  .services li::before{content:"";width:9px;height:9px;border-radius:50%;background:var(--gold);margin-right:14px;box-shadow:0 0 0 2px rgba(234,181,74,.35)}
  .services-scope{left:53px;top:664px;color:var(--gold);font-weight:600;font-size:13.5px;line-height:17.5px}
  .callbar{left:46px;top:733px;width:456px;height:43px;background:linear-gradient(90deg,var(--gold),var(--gold-deep));border-radius:14px 14px 0 0;display:flex;align-items:center;justify-content:center;gap:9px;color:#fff}
  .callbar .lead{font-weight:700;font-size:14.5px}
  .callbar .phone{font-weight:700;font-size:20px}

  /* back */
  .copy{font-size:10.3px;line-height:13.9px;color:var(--ink)}
  .copy p{margin-bottom:13px}
  .copy-top{left:296px;top:42px;width:224px}
  .copy-mid{left:39px;top:266px;width:232px}
  .slogan{left:260px;top:550px;font-weight:700;font-style:italic;font-size:10.6px;line-height:14.5px;transform:rotate(-4deg);transform-origin:left top}
  .cta{left:285px;top:638px;color:var(--gold);font-family:"Jost",sans-serif;font-weight:700;font-size:18px}
  .cta-rule{left:364px;top:662px}
  .contact{left:286px;top:676px;color:#fff;font-size:10.5px;border-collapse:collapse}
  .contact td{padding:0;height:16px}
  .contact .label{color:var(--gold);font-weight:700;width:36px}
  .contact .sep{width:11px}
  .address{left:286px;top:731px;color:#fff;font-size:8.6px;line-height:13.7px;width:190px}
</style>
</head>
<body>

<section class="page page--front">
  <svg class="shapes" viewBox="0 0 548 776" aria-hidden="true">
    <defs>
      <linearGradient id="scene" x1="0" y1="0" x2="0" y2="1">
        <stop offset="0" stop-color="#ffffff"/>
        <stop offset=".25" stop-color="#8fa886"/>
        <stop offset=".6" stop-color="#4f6a52"/>
        <stop offset="1" stop-color="#3b4a5c"/>
      </linearGradient>
    </defs>
    <rect x="0" y="150" width="548" height="380" fill="url(#scene)" role="img" aria-label="Foto: Familie vor Haus mit Solardach und E-Auto an der Ladestation"/>
    <path d="M0 362 C120 410 300 400 548 340 V548 H0 Z" fill="var(--gold)"/>
    <path d="M0 420 C140 430 330 410 548 357 V776 H0 Z" fill="var(--navy)"/>
    <circle cx="458" cy="80" r="120" fill="var(--gold)"/>
    <circle cx="468" cy="72" r="114" fill="var(--navy)"/>
  </svg>

  <h1 class="abs headline">STARK WIE<br>DIE SONNE-<br><span class="accent">IHRE VORTEILE!</span></h1>

  <div class="abs brand-dot"></div>
  <div class="abs brand">SOLVARA</div>

  <figure class="polaroid" style="left:48px;top:288px;width:168px;height:112px;transform:rotate(-3deg)">
    <div class="fill" role="img" aria-label="Foto: Frau jubelt zwischen Solarmodulen" style="background:linear-gradient(180deg,#eef1f3,#7fa0b2 55%,#2c3645)"></div>
  </figure>
  <figure class="polaroid" style="left:68px;top:378px;width:172px;height:128px;transform:rotate(-5deg)">
    <div class="fill" role="img" aria-label="Foto: Solarmodul im Gras" style="background:linear-gradient(180deg,#9db46d,#343941 40%,#2a2e35 80%,#8aa35a)"></div>
  </figure>

  <div class="abs intro">
    <p><span class="company">SOLVARA GmbH</span> gewährleistet nicht nur höchste Qualität und Effizienz bei der Umsetzung, sondern sorgen auch dafür, dass alle geltenden Normen und Baugesetze eingehalten werden. Die Einhaltung dieser Standards ist entscheidend für eine reibungslose und sichere Installation.</p>
    <p>Unsere langjährige Erfahrung ermöglicht es uns, maßgeschneiderte Anlagen zu entwickeln, die exakt auf Ihre Bedürfnisse zugeschnitten sind.</p>
    <p>Von der Planung bis zur Inbetriebnahme legen wir großen Wert darauf, Lösungen zu schaffen, die nicht nur effektiv, sondern auch kosteneffizient sind.</p>
    <p>Entscheiden Sie sich für unsere Expertise, um die umfassenden Vorteile einer maßgeschneiderten, normgerechten Lösung zu genießen.</p>
  </div>

  <div class="abs services-label">spezialisiert in den Bereichen:</div>
  <ul class="abs services">
    <li>Erstberatung</li>
    <li>Planung</li>
    <li>Errichtung</li>
    <li>Förderabwicklung</li>
  </ul>
  <div class="abs services-scope">von PV-Anlagen, Stromspeicher<br>und Ladeinfrastruktur</div>

  <div class="abs callbar"><span class="lead">wir unterstützen Sie gerne:</span><span class="phone">+43 (0) 660 218 57 30</span></div>
</section>

<section class="page page--back">
  <svg class="shapes" viewBox="0 0 548 776" aria-hidden="true">
    <defs>
      <linearGradient id="storage" x1="0" y1="0" x2="1" y2="1">
        <stop offset="0" stop-color="#4a5560"/>
        <stop offset=".45" stop-color="#d9dcdf"/>
        <stop offset="1" stop-color="#5d6770"/>
      </linearGradient>
      <linearGradient id="team" x1="0" y1="0" x2="0" y2="1">
        <stop offset="0" stop-color="#c9a27f"/>
        <stop offset=".45" stop-color="#252838"/>
        <stop offset="1" stop-color="#1a1c28"/>
      </linearGradient>
    </defs>
    <path d="M0 0 H283 C280 140 180 232 0 238 Z" fill="var(--gold)"/>
    <path d="M0 0 H272 C268 125 165 205 0 212 Z" fill="url(#storage)" role="img" aria-label="Foto: Stromspeicher und Wallbox an der Wand"/>
    <path d="M0 574 C200 640 380 610 548 564 V776 H0 Z" fill="var(--gold)"/>
    <path d="M0 616 C190 660 390 630 548 572 V776 H0 Z" fill="var(--navy)"/>
    <rect x="10" y="588" width="255" height="188" fill="url(#team)" role="img" aria-label="Foto: drei Mitarbeiter im Firmenpolo"/>
  </svg>

  <div class="abs copy copy-top">
    <p>Die Installation von Photovoltaikanlagen bietet Ihnen die Möglichkeit, Ihren ökologischen Fußabdruck zu minimieren und langfristige finanzielle Vorteile zu erzielen.</p>
    <p>Durch die Nutzung der Sonnenenergie können Sie Ihre Energiekosten erheblich senken und sogar überschüssigen Strom ins Netz einspeisen, wodurch Sie zusätzliches Einkommen generieren. Photovoltaik ist eine nachhaltige und zukunftsfähige Investition.</p>
    <p>Unsere erfahrenen Experten stehen Ihnen zur Verfügung, um Ihnen den Weg zur optimalen Photovoltaiklösung für Ihr Zuhause oder Ihr Unternehmen zu ebnen.</p>
  </div>

  <div class="abs copy copy-mid">
    <p>Entdecken Sie die Vorteile einer ganzheitlichen Energielösung für Ihr Zuhause!</p>
    <p>Optimieren Sie Ihre Photovoltaikanlage durch die Integration eines Energiespeichers, einer Ladeinfrastruktur für Ihr Elektrofahrzeug und einer effizienten Warmwasseraufbereitung.</p>
    <p>Mit einem Energiespeicher können Sie Ihren selbst erzeugten Solarstrom speichern und flexibel nutzen, um Ihre Stromkosten zu reduzieren oder laden Sie Ihr Elektrofahrzeug direkt mit grünem Strom und senken Sie Ihre Mobilitätskosten.</p>
    <p>Die Einbindung einer Warmwasseraufbereitung ermöglicht es, Ihren Warmwasserbedarf durch Solarenergie zu decken, was zu einer nachhaltigen und kostengünstigen Energieversorgung führt.</p>
  </div>

  <figure class="polaroid" style="left:290px;top:278px;width:184px;height:120px;transform:rotate(3deg)">
    <div class="fill" role="img" aria-label="Foto: Ladekabel wird an ein E-Auto gesteckt" style="background:linear-gradient(90deg,#3d4654,#8c96a0 50%,#2f5a33)"></div>
  </figure>
  <figure class="polaroid" style="left:322px;top:390px;width:186px;height:136px;transform:rotate(-4deg)">
    <div class="fill" role="img" aria-label="Foto: Luftaufnahme einer Halle mit Solardach" style="background:linear-gradient(160deg,#8a7356,#3c5576 45%,#d5d8dc 70%,#7d6a52)"></div>
  </figure>

  <div class="abs slogan">Erleben Sie die Zukunft der<br>Energieeffizienz – wir beraten Sie gerne<br>für eine maßgeschneiderte Lösung!</div>

  <div class="abs cta">JETZT DIE SONNE NUTZEN !</div>
  <svg class="abs cta-rule" width="64" height="8" viewBox="0 0 64 8" aria-hidden="true">
    <path d="M2 2 H62 M6 6 H58" stroke="var(--gold)" stroke-width="1.6" stroke-linecap="round"/>
  </svg>

  <table class="abs contact">
    <tr><td class="label">Mail</td><td class="sep">:</td><td>office@solvara-pv.at</td></tr>
    <tr><td class="label">Tel.</td><td class="sep">:</td><td>+43 (0) 660 218 57 30</td></tr>
    <tr><td class="label">Web</td><td class="sep">:</td><td>www.solvara-pv.at</td></tr>
  </table>
  <div class="abs address">SOLVARA GmbH, Lindenweg 12, A-9020 Sonnfeld</div>
</section>

</body>
</html>
```